Letterhead Design Project

I need letterhead designed for my law firm. It would also be used for web based stuff as well.

Industry/Entity Type

Law Firm

```html
<!DOCTYPE html>
<html lang="en">
<head>
<meta charset="utf-8">
<title>Hartwell &amp; Osei — Letterhead</title>
<link href="https://fonts.googleapis.com/css2?family=Questrial&display=swap" rel="stylesheet">
<style>
  :root {
    --backdrop: #e4e4e4;
    --paper: #ffffff;
    --ink: #3a3a3a;
    --ink-soft: #555555;
    --brand-dark: #2f3a3d;
    --brand-accent: #1f9ac4;
    --rule: #6a6a6a;
  }
  * { box-sizing: border-box; margin: 0; padding: 0; }
  html, body {
    width: 1200px;
    height: 968px;
    overflow: hidden;
    background: var(--backdrop);
    font-family: "Questrial", "Century Gothic", sans-serif;
    color: var(--ink);
  }
  .letterhead {
    position: absolute;
    left: 260px;
    top: 42px;
    width: 680px;
    height: 884px;
    background: var(--paper);
    box-shadow: 0 2px 10px rgba(0,0,0,0.08);
  }
  .brand {
    position: absolute;
    top: 58px;
    left: 372px;
    display: flex;
    align-items: center;
    gap: 10px;
  }
  .brand__square {
    width: 14px;
    height: 14px;
    background: var(--brand-accent);
  }
  .brand__name {
    font-size: 21px;
    letter-spacing: 0.08em;
    text-transform: uppercase;
    color: var(--brand-dark);
    white-space: nowrap;
  }
  .contact-bar {
    position: absolute;
    left: 70px;
    right: 70px;
    bottom: 60px;
    display: flex;
    align-items: center;
    justify-content: space-between;
    font-size: 10.5px;
    line-height: 1.45;
    color: var(--ink-soft);
  }
  .contact-bar__divider {
    width: 1px;
    height: 26px;
    background: var(--rule);
  }
  .contact-bar__label { font-weight: 700; color: var(--ink); }
</style>
</head>
<body>
  <main class="letterhead">
    <header class="brand">
      <span class="brand__square"></span>
      <span class="brand__name">Hartwell &amp; Osei</span>
    </header>

    <footer class="contact-bar">
      <address class="contact-bar__address" style="font-style:normal">
        812 Linden Avenue NW<br>
        Washington, DC 20005
      </address>
      <span class="contact-bar__divider"></span>
      <div class="contact-bar__phones">
        <span class="contact-bar__label">Phone:</span> (202) 555-0148<br>
        <span class="contact-bar__label">Toll Free:</span> 855-555-0172
      </div>
      <span class="contact-bar__divider"></span>
      <div class="contact-bar__web">
        www.hartwellosei.com<br>
        info@hartwellosei.com
      </div>
    </footer>
  </main>
</body>
</html>
```